Fallowmere community hall home page

We are building a modern, responsive website & booking system for our community hall. For this SketchHarbor task, we would like to receive design ideas for the home page.
There are no limits on the colours or fonts that can be used. We are looking for a modern, fresh design with a local/community feel. We don’t have a logo but we also recognise that our name is quite long! … So initials (FCH) instead of the name would be fine.
People book our community hall for a range of activities including: fitness classes, wedding receptions, birthday parties, business meetings, teaching, community events, charity fundraisers and other celebrations.
We have three main goals for the website. The first is that people can check our calendar and make a booking for an available time slot. The second is that they can read about our facilities and the prices for hiring them. The third is that people can find out about upcoming activities & events.
CTA: Book now
A button that links to a booking request form. (The form is not part of this design project)
Primary/Header navigation:
Home | Calendar | Facilities | Prices | Photos | News | Contact
Secondary/Footer navigation:
Chatterbook | Quipper
Login | Register | Privacy policy | Terms & conditions
Example texts (lorem ipsum etc. is also fine):
We have everything you need from a venue, whether it’s an elegant room with ample flexible space, a lavish and elegant hall for a wedding reception, a conference room that fits 125 delegates or a easy access venue to the town centre.
The hall is available for hire for wedding receptions, birthday celebrations, anniversaries, children's parties, presentations, lectures, fitness groups, and will comfortably accommodate all your guests.
This venue is well equipped with a modern kitchen, a range of audio and technical services, hearing loop, licensed bar, conference facilities, disabled access and unlimited free WiFi.
You can use this website to find out more about our rooms, equipment and the services we can offer and use the calendar to see where we have rooms available. You can also book rooms using our online booking system.
To the front of the building is a large public open grassed area across which is a row of shops. To the rear of the building is the large car park, including spaces for blue badge holders and a large enclosed cycle rack. This area also has extensive gardens, with seating and planting areas maintained by local volunteers.
The community hall is run and managed by volunteers of the Fallowmere Community Organisation. Our objectives are to increase opportunities for people living in and around Fallowmere.
We are passionate about being the heart of the community; caring for this community centred property and visitors are at the heart of all we do.
Where to go next
— Check when the hall is free
— Read our booking policy documents
— Make a booking reservation
Amenities
— Free WiFi
— Free car parking
— Fully equipped kitchen
— Hearing loop
Details for our most popular facilities (rooms):
Name: Main hall
Short description: A 127 square metre main hall with entrance lobby, toilets, a well-equipped kitchen and separate storage facilities. Three sets of double doors provide access to a large paved area and the adjacent playing field.
Capacity: 180 people
Price: £10-20 per hour
Links: More info | Book now
Name: Large meeting room
Short description: A delightful, spacious room with an outlook and access to the small walled garden. Ideal for meetings and small gatherings - it has its own access door and the use of a disabled W/C. We offer a reduced rate for this room when booked together with the main hall.
Capacity: 20 people
Price: £6-12 per hour
Attachments:
We have attached some photos of the hall & some (royalty free) stock images for inspiration.

```html
<!DOCTYPE html>
<html lang="en">
<head>
<meta charset="utf-8">
<title>Fallowmere Community Hall</title>
<link rel="stylesheet" href="https://fonts.googleapis.com/css2?family=Playfair+Display:wght@400;700;900&family=Open+Sans:wght@400;600&display=swap">
<style>
:root{
  --ink:#333333;
  --text:#3a3a3a;
  --muted:#555555;
  --paper:#ffffff;
  --line:#3a3a3a;
  --footer:#333333;
  --serif:'Playfair Display', Georgia, serif;
  --sans:'Open Sans', Arial, sans-serif;
}
*{box-sizing:border-box;margin:0;padding:0}
html,body{width:1200px;height:2172px;overflow:hidden;background:var(--paper)}
body{position:relative;font-family:var(--sans);color:var(--text)}
.abs{position:absolute}
a{color:inherit;text-decoration:none}

.brand{left:66px;top:12px;font-family:var(--sans);font-weight:400;font-size:24px;letter-spacing:6px;color:var(--ink)}
.main-nav{top:13px;left:0;font-size:12.5px;color:var(--ink)}
.main-nav a{position:absolute;white-space:nowrap}
.btn-dark{background:var(--ink);color:#fff;display:flex;align-items:center;justify-content:center;font-size:9.5px}
.book-top{left:1066px;top:9px;width:65px;height:23px;font-size:8.5px}
.side-rule{left:185px;top:33px;width:1px;height:537px;background:var(--line)}
.side-login{left:69px;top:428px;width:84px;height:30px}
.side-register{left:69px;top:469px;width:83px;height:31px}

.hero{left:226px;top:37px;width:906px;height:463px;background:linear-gradient(160deg,#cfc6ad 0%,#8f7d5e 35%,#e8e2d6 60%,#6e5637 100%)}
.hero-arrow{width:20px;height:20px}
.hero-prev{left:1046px;top:452px;border:1px solid #fff}
.hero-next{left:1079px;top:452px;background:#fff}

.title{left:220px;top:515px;font-family:var(--serif);font-weight:700;font-size:47px;line-height:58px;letter-spacing:3.5px;color:var(--ink);white-space:nowrap}
.tagline{left:961px;top:519px;font-size:11.5px;color:var(--ink)}
.tagline-rule{left:961px;top:548px;width:167px;height:1px;background:var(--line)}
.tagline-list{left:961px;top:558px;width:178px;font-size:9px;line-height:16.7px;color:var(--muted)}

.section-head{font-family:var(--serif);font-weight:700;font-size:24px;line-height:31px;letter-spacing:1px;color:var(--ink)}
.book-head{left:48px;top:697px;text-align:center;width:126px}
.book-rule{left:0;top:772px;width:310px;height:1px;background:var(--line)}
.booking-bar{left:335px;top:728px;width:686px;height:87px;border:2px solid var(--ink)}
.field{top:752px}
.field-label{font-family:var(--serif);font-weight:700;font-size:14.5px;color:var(--ink);letter-spacing:.5px}
.field-value{margin-top:4px;font-size:9px;text-decoration:underline;color:var(--ink)}
.field-divider{top:755px;width:1px;height:34px;background:var(--line)}
.search-btn{left:929px;top:746px;width:55px;height:51px;background:var(--ink);display:flex;align-items:center;justify-content:center}

.intro{left:296px;top:886px;width:758px;text-align:center;font-size:13.6px;line-height:26.4px;color:#222}

.fac-head{left:20px;top:1043px;width:147px;text-align:right}
.fac-rule{left:0;top:1146px;width:173px;height:1px;background:var(--line)}
.card{top:1049px;width:276px;height:447px;border:2px solid var(--ink);background:#fff;box-shadow:4px 5px 10px rgba(0,0,0,.12);text-align:center}
.card-photo{position:relative;height:182px}
.card-photo::after{content:"";position:absolute;left:21px;top:21px;right:23px;bottom:20px;border:1px solid rgba(255,255,255,.85)}
.photo-hall{background:linear-gradient(180deg,#2d2a6b 0%,#8b4fb0 25%,#3b3340 60%,#24202a 100%)}
.photo-meeting{background:linear-gradient(180deg,#f2f2f2 0%,#d7d4cf 55%,#8a6f4e 80%,#2f3f6b 100%)}
.card-title{margin-top:8px;font-family:var(--serif);font-weight:700;font-size:16px;letter-spacing:1px;color:var(--ink)}
.card-text{margin:6px auto 0;width:240px;font-size:10.6px;line-height:18.6px;color:var(--muted)}
.card-meta{margin-top:18px;font-size:10.6px;line-height:18.6px;color:var(--muted)}
.card-actions{position:absolute;left:0;right:0;bottom:18px;display:flex;justify-content:center;gap:9px}
.btn-outline,.btn-solid{width:83px;height:31px;display:flex;align-items:center;justify-content:center;font-size:9.5px}
.btn-outline{border:2px solid var(--ink);color:var(--ink)}
.btn-solid{background:var(--ink);color:#fff}

.list-head{font-family:var(--serif);font-weight:700;font-size:23px;letter-spacing:1px;color:var(--ink)}
.next-rule{left:0;top:1602px;width:327px;height:1px;background:var(--line)}
.tick-list{list-style:none;font-size:14px;color:var(--ink)}
.tick-list li{display:flex;align-items:center;height:31.7px;gap:10px}

.event-card{left:360px;top:1808px;width:477px;height:187px;background:#fff;border:2px solid var(--ink);z-index:2}
.event-kicker{left:50px;top:27px;font-size:10.5px;letter-spacing:.5px;color:var(--ink)}
.event-value{font-family:var(--serif);font-weight:700;font-size:23px;letter-spacing:1.5px;color:var(--ink);white-space:nowrap}
.event-label{font-size:10.5px;letter-spacing:.5px;color:var(--ink);margin-top:2px}
.event-divider{top:77px;width:1px;height:30px;background:var(--line)}
.dash{top:148px;height:2px;width:16px}

.footer{left:0;top:1940px;width:1200px;height:232px;background:var(--footer);color:#fff}
.footer-brand{left:64px;top:76px;font-family:var(--sans);font-weight:400;font-size:24px;letter-spacing:6px}
.footer-rule{left:183px;top:55px;width:1px;height:163px;background:#fff}
.social{left:30px;top:170px;display:flex;gap:12px;font-size:11px}
.footer-login{left:447px;top:79px;width:144px;height:51px;background:#fff;color:var(--ink);display:flex;align-items:center;justify-content:center;font-size:17px}
.footer-register{left:605px;top:79px;width:140px;height:51px;border:2px solid #fff;display:flex;align-items:center;justify-content:center;font-size:17px}
.footer-nav a{position:absolute;font-size:11.5px;white-space:nowrap;top:166px}
.footer-nav-rule{left:448px;top:192px;width:679px;height:1px;background:#fff}
.legal a{position:absolute;top:206px;font-size:10.5px;white-space:nowrap}
</style>
</head>
<body>

<header>
  <div class="abs brand">FCH</div>
  <nav class="abs main-nav">
    <a style="left:556px">Home</a>
    <a style="left:623px">Calendar</a>
    <a style="left:707px">Facilities</a>
    <a style="left:788px">Prices</a>
    <a style="left:854px">Photos</a>
    <a style="left:926px">News</a>
    <a style="left:989px">Contact</a>
  </nav>
  <a class="abs btn-dark book-top">Book now</a>
  <div class="abs side-rule"></div>
  <a class="abs btn-dark side-login">Log in</a>
  <a class="abs btn-dark side-register">Register</a>
</header>

<section>
  <div class="abs hero" role="img" aria-label="Elegant function room laid with round tables, white cloths and gold chairs under a chandelier"></div>
  <svg class="abs hero-arrow hero-prev" viewBox="0 0 20 20"><path d="M12 5 7 10l5 5" fill="none" stroke="#fff" stroke-width="1.6"/></svg>
  <svg class="abs hero-arrow hero-next" viewBox="0 0 20 20"><path d="M8 5l5 5-5 5" fill="none" stroke="#333" stroke-width="1.6"/></svg>

  <h1 class="abs title">Fallowmere<br>Community Hall</h1>
  <div class="abs tagline">Community Hall Booking</div>
  <div class="abs tagline-rule"></div>
  <p class="abs tagline-list">fitness classes, wedding receptions, birthday parties, business meetings, teaching, community events, charity fundraisers and other celebrations.</p>
</section>

<section>
  <h2 class="abs section-head book-head">Book your event now</h2>
  <div class="abs book-rule"></div>
  <div class="abs booking-bar"></div>
  <div class="abs field" style="left:372px"><div class="field-label">Date</div><div class="field-value">Set date</div></div>
  <svg class="abs" style="left:442px;top:774px" width="19" height="17" viewBox="0 0 19 17"><rect x="1" y="1" width="17" height="15" rx="2" fill="none" stroke="#333" stroke-width="1.3"/><path d="M1 5h17" stroke="#333" stroke-width="1.3"/><g fill="#333"><rect x="4" y="7" width="2" height="2"/><rect x="8" y="7" width="2" height="2"/><rect x="12" y="7" width="2" height="2"/><rect x="4" y="11" width="2" height="2"/><rect x="8" y="11" width="2" height="2"/><rect x="12" y="11" width="2" height="2"/></g></svg>
  <div class="abs field-divider" style="left:511px"></div>
  <div class="abs field" style="left:548px"><div class="field-label">Activity</div><div class="field-value">Fitness Classes</div></div>
  <svg class="abs" style="left:646px;top:775px" width="17" height="17" viewBox="0 0 17 17"><circle cx="8.5" cy="8.5" r="7.5" fill="none" stroke="#333" stroke-width="1.3"/><path d="M5 7h7l-3.5 4z" fill="#333"/></svg>
  <div class="abs field-divider" style="left:687px"></div>
  <div class="abs field" style="left:723px"><div class="field-label">Venue</div><div class="field-value">Conference Room</div></div>
  <svg class="abs" style="left:837px;top:774px" width="20" height="17" viewBox="0 0 20 17"><path d="M1.5 8.5 10 1.5l8.5 7V16h-17z" fill="none" stroke="#333" stroke-width="1.2"/></svg>
  <a class="abs search-btn" aria-label="Search">
    <svg width="20" height="20" viewBox="0 0 20 20"><circle cx="8.5" cy="8.5" r="6" fill="none" stroke="#fff" stroke-width="1.6"/><path d="M13 13l5 5" stroke="#fff" stroke-width="1.6"/></svg>
  </a>

  <p class="abs intro">We have everything you need from a venue, whether it’s an elegant room with ample flexible space, a lavish and elegant hall for a wedding reception, a conference room that fits 125 delegates or a easy access venue to the town centre. The hall is available for hire for wedding receptions, birthday celebrations, anniversaries, children's parties, presentations, lectures, fitness groups, and will comfortably accommodate all your guests.</p>
</section>

<section>
  <h2 class="abs section-head fac-head">Our most popular facilities:</h2>
  <div class="abs fac-rule"></div>

  <article class="abs card" style="left:221px">
    <div class="card-photo photo-hall" role="img" aria-label="Main hall with guests seated at round tables under purple lighting"></div>
    <h3 class="card-title">Main Hall</h3>
    <p class="card-text">A 127 square metre main hall with entrance lobby, toilets, a well-equipped kitchen and separate storage facilities. Three sets of double doors provide access to a large paved area and the adjacent playing field.</p>
    <p class="card-meta">Capacity: 180 people<br>Price: £10-20 per hour</p>
    <div class="card-actions"><a class="btn-outline">More info</a><a class="btn-solid">Book now</a></div>
  </article>

  <article class="abs card" style="left:539px">
    <div class="card-photo photo-meeting" role="img" aria-label="Large meeting room with a long conference table and projector screen"></div>
    <h3 class="card-title">Large meeting room</h3>
    <p class="card-text">A delightful, spacious room with an outlook and access to the small walled garden. Ideal for meetings and small gatherings - it has its own access door and the use of a disabled W/C. We offer a reduced rate for this room when booked together with the main hall.</p>
    <p class="card-meta">Capacity: 20 people<br>Price: £6-12 per hour</p>
    <div class="card-actions"><a class="btn-outline">More info</a><a class="btn-solid">Book now</a></div>
  </article>

  <article class="abs card" style="left:854px">
    <div class="card-photo photo-hall" role="img" aria-label="Main hall with guests seated at round tables under purple lighting"></div>
    <h3 class="card-title">Main Hall</h3>
    <p class="card-text">A 127 square metre main hall with entrance lobby, toilets, a well-equipped kitchen and separate storage facilities. Three sets of double doors provide access to a large paved area and the adjacent playing field.</p>
    <p class="card-meta">Capacity: 180 people<br>Price: £10-20 per hour</p>
    <div class="card-actions"><a class="btn-outline">More info</a><a class="btn-solid">Book now</a></div>
  </article>
</section>

<section>
  <div class="abs next-rule"></div>
  <h2 class="abs list-head" style="left:338px;top:1577px">Where to go next</h2>
  <ul class="abs tick-list" style="left:338px;top:1621px">
    <li><svg width="22" height="22" viewBox="0 0 22 22"><circle cx="11" cy="11" r="11" fill="#333"/><path d="M6.5 11.5l3 3 6-6" fill="none" stroke="#fff" stroke-width="2"/></svg>Check when the hall is free</li>
    <li><svg width="22" height="22" viewBox="0 0 22 22"><circle cx="11" cy="11" r="11" fill="#333"/><path d="M6.5 11.5l3 3 6-6" fill="none" stroke="#fff" stroke-width="2"/></svg>Read our booking policy documents</li>
    <li><svg width="22" height="22" viewBox="0 0 22 22"><circle cx="11" cy="11" r="11" fill="#333"/><path d="M6.5 11.5l3 3 6-6" fill="none" stroke="#fff" stroke-width="2"/></svg>Make a booking reservation</li>
  </ul>

  <h2 class="abs list-head" style="left:790px;top:1576px">Amenities</h2>
  <ul class="abs tick-list" style="left:790px;top:1621px">
    <li><svg width="22" height="22" viewBox="0 0 22 22"><circle cx="11" cy="11" r="11" fill="#333"/><path d="M6.5 11.5l3 3 6-6" fill="none" stroke="#fff" stroke-width="2"/></svg>Free WiFi</li>
    <li><svg width="22" height="22" viewBox="0 0 22 22"><circle cx="11" cy="11" r="11" fill="#333"/><path d="M6.5 11.5l3 3 6-6" fill="none" stroke="#fff" stroke-width="2"/></svg>Free car parking</li>
    <li><svg width="22" height="22" viewBox="0 0 22 22"><circle cx="11" cy="11" r="11" fill="#333"/><path d="M6.5 11.5l3 3 6-6" fill="none" stroke="#fff" stroke-width="2"/></svg>Fully equipped kitchen</li>
    <li><svg width="22" height="22" viewBox="0 0 22 22"><circle cx="11" cy="11" r="11" fill="#333"/><path d="M6.5 11.5l3 3 6-6" fill="none" stroke="#fff" stroke-width="2"/></svg>Hearing loop</li>
  </ul>
</section>

<section class="abs event-card">
  <div class="abs event-kicker">Upcomming event:&nbsp; Wedding reception</div>
  <div class="abs" style="left:50px;top:62px"><div class="event-value">02 Feb</div><div class="event-label">Date</div></div>
  <div class="abs event-divider" style="left:161px"></div>
  <div class="abs" style="left:186px;top:62px"><div class="event-value">Main hall</div><div class="event-label">Venue</div></div>
  <div class="abs event-divider" style="left:319px"></div>
  <div class="abs" style="left:344px;top:62px"><div class="event-value">20:00</div><div class="event-label">Time</div></div>
  <div class="abs dash" style="left:52px;background:#333"></div>
  <div class="abs dash" style="left:77px;background:#bbb"></div>
  <div class="abs dash" style="left:102px;background:#bbb"></div>
</section>

<footer class="abs footer">
  <div class="abs footer-brand">FCH</div>
  <div class="abs footer-rule"></div>
  <div class="abs social"><a>Chatterbook</a><a>Quipper</a></div>
  <a class="abs footer-login">Log in</a>
  <a class="abs footer-register">Register</a>
  <nav class="footer-nav">
    <a style="left:489px">HOME</a>
    <a style="left:576px">CALENDAR</a>
    <a style="left:688px">FACILITIES</a>
    <a style="left:796px">PRICES</a>
    <a style="left:886px">PHOTOS</a>
    <a style="left:985px">NEWS</a>
    <a style="left:1071px">CONTACT</a>
  </nav>
  <div class="abs footer-nav-rule"></div>
  <nav class="legal">
    <a style="left:876px">PRIVACY POLICY</a>
    <a style="left:1009px">TERMS &amp; CONDITIONS</a>
  </nav>
</footer>

</body>
</html>
```